Harwell Properties Business Cards

I would like a business card that includes myself and my partner.
Includes: Logo, office #, email, website, our names, our numbers and possibly the address. I would also like the logo to be embossed and the card to be horizontal.
There is a photo of our yard signs to give you an idea of the colors of our business.

Target Market(s)

Everyone in real estate market.
We are in a rural area. Our clientele are from all socioeconomic backgrounds.

Industry/Entity Type

Real Estate Agent

Contact Information for Business Card

Company Name: Harwell Properties
Our Names, Titles & Cell #'s : Dana Harwell-Broker (555).613.2947, Marla Harwell-Realtor (555).730.5816
Office #: (555).264.1300
Website: harwellproperties.example
Joint Email: harwell@harwellproperties.example
Office Address: 418C W. Pell Creek St.
Calloway, TX. 00518

Font styles to use
Serif

Requirements
Must have
• HORIZONTAL, Logo, Myself and my partners names, Our cell #'s, our office #, our website, our email address
Nice to have
• Embossed logo, office address, our titles.

```html
<!DOCTYPE html>
<html lang="en">
<head>
<meta charset="utf-8">
<title>Harwell Properties Business Card</title>
<link rel="stylesheet" href="https://fonts.googleapis.com/css2?family=Lora:wght@400;700&display=swap">
<style>
  :root {
    --plum: #3b2150;
    --paper: #ffffff;
    --backdrop: #ecebef;
    --ink: #2c1a3b;
  }
  * { box-sizing: border-box; margin: 0; padding: 0; }
  html, body {
    width: 1200px; height: 799px; overflow: hidden;
    background: var(--backdrop);
    font-family: "Lora", Georgia, serif;
    color: var(--ink);
  }
  .card {
    position: absolute; left: 100px; top: 114px;
    width: 1000px; height: 571px;
    background: var(--paper);
    overflow: hidden;
    box-shadow: 0 10px 30px rgba(40, 20, 60, 0.18);
  }
  .skyline {
    position: absolute; left: 0; top: 0; width: 100%; height: 96px;
    background: linear-gradient(90deg, var(--plum) 0%, #4a2d62 50%, var(--plum) 100%);
  }
  .base-band {
    position: absolute; left: 0; bottom: 0; width: 100%; height: 52px;
    background: var(--plum);
  }
  .brand {
    position: absolute; left: 48px; top: 122px;
    display: flex; align-items: center; gap: 16px;
  }
  .brand-mark {
    width: 58px; height: 58px; border-radius: 50%;
    background: var(--plum);
  }
  .brand-name {
    font-weight: 700; color: var(--plum);
    line-height: 1;
  }
  .brand-name .primary { display: block; font-size: 44px; letter-spacing: 1px; text-transform: uppercase; }
  .brand-name .secondary {
    display: block; font-size: 28px; margin-top: 6px; padding-top: 6px;
    border-top: 2px solid var(--plum); text-align: center;
  }
  .contact-list {
    position: absolute; left: 52px; top: 250px;
    list-style: none; font-size: 17px; font-weight: 700;
  }
  .contact-list li { display: flex; align-items: flex-start; gap: 14px; margin-bottom: 10px; }
  .contact-list svg { width: 22px; height: 22px; flex: none; }
  .contact-list .address span { display: block; line-height: 1.35; }
  .team {
    position: absolute; right: 60px; top: 250px; width: 340px; text-align: right;
  }
  .member-name { font-size: 24px; font-weight: 700; letter-spacing: 1px; text-transform: uppercase; }
  .member-role, .member-phone { font-size: 20px; line-height: 1.2; }
  .team-divider { border: 0; border-top: 1.5px solid var(--ink); width: 200px; margin: 16px 0 16px auto; }
</style>
</head>
<body>
  <main class="card">
    <div class="skyline" role="img" aria-label="City skyline silhouette across the top of the card"></div>

    <div class="brand">
      <span class="brand-mark" aria-hidden="true"></span>
      <div class="brand-name">
        <span class="primary">Harwell</span>
        <span class="secondary">Properties</span>
      </div>
    </div>

    <ul class="contact-list">
      <li>
        <svg viewBox="0 0 24 24" aria-hidden="true"><circle cx="12" cy="12" r="12" fill="var(--plum)"/><path d="M8.5 6.5l2 2-1.2 1.6a7 7 0 0 0 4.6 4.6l1.6-1.2 2 2-1.3 1.8C11.8 17.6 6.4 12.2 6.7 7.8z" fill="#fff"/></svg>
        <span>(555).264.1300</span>
      </li>
      <li>
        <svg viewBox="0 0 24 24" aria-hidden="true"><circle cx="12" cy="12" r="12" fill="var(--plum)"/><circle cx="12" cy="12" r="6" fill="none" stroke="#fff" stroke-width="1.4"/><ellipse cx="12" cy="12" rx="2.6" ry="6" fill="none" stroke="#fff" stroke-width="1.2"/><line x1="6" y1="12" x2="18" y2="12" stroke="#fff" stroke-width="1.2"/></svg>
        <span>harwellproperties.example</span>
      </li>
      <li>
        <svg viewBox="0 0 24 24" aria-hidden="true"><circle cx="12" cy="12" r="12" fill="var(--plum)"/><rect x="6" y="8" width="12" height="8" fill="#fff"/><path d="M6 8l6 5 6-5" fill="none" stroke="var(--plum)" stroke-width="1.2"/></svg>
        <span>harwell@harwellproperties.example</span>
      </li>
      <li class="address">
        <svg viewBox="0 0 24 24" aria-hidden="true"><circle cx="12" cy="12" r="12" fill="var(--plum)"/><path d="M12 5.5a4.5 4.5 0 0 0-4.5 4.5c0 3.4 4.5 8.5 4.5 8.5s4.5-5.1 4.5-8.5A4.5 4.5 0 0 0 12 5.5z" fill="#fff"/><circle cx="12" cy="10" r="1.6" fill="var(--plum)"/></svg>
        <div><span>418C W. Pell Creek St.</span><span>Calloway, TX. 00518</span></div>
      </li>
    </ul>

    <section class="team">
      <div class="member">
        <p class="member-name">Dana Harwell</p>
        <p class="member-role">Broker</p>
        <p class="member-phone">(555).613.2947</p>
      </div>
      <hr class="team-divider">
      <div class="member">
        <p class="member-name">Marla Harwell</p>
        <p class="member-role">Realtor</p>
        <p class="member-phone">(555).730.5816</p>
      </div>
    </section>

    <div class="base-band"></div>
  </main>
</body>
</html>
```